Dune Business Card Design Project

We have an existing business card. We are looking to creat a new card for the store. I have attached a my own business so you have a refference of what the current card looks like.

Phone: 1300 574 213
email: merrow@dunepanes.com.au
website: www.dunepanes.com.au
Address: (Inside Merrow Rug Hall) 418 Tolvey Rd, Pelbrook VIC 3158
Updates

This is a new business card for our store.

Industry/Entity Type

Business

Requirements
Must have
• Must look similar to the existing card

```html
<!DOCTYPE html>
<html lang="en">
<head>
<meta charset="utf-8">
<title>Dune Shutters &amp; Blinds – Business Cards</title>
<link rel="stylesheet" href="https://fonts.googleapis.com/css2?family=Open+Sans:wght@400;700&display=swap">
<style>
  :root {
    --page-bg: #d9d9d7;
    --card-white: #fbfbfa;
    --band-cream: #ecebe2;
    --ink: #141414;
    --ink-soft: #2b2b2b;
    --tag-grey: #5a5a5a;
    --accent-red: #d21f3c;
    --dot-blue: #7fc6e4;
    --dot-red: #d21f3c;
    --dot-yellow: #c9a80f;
    --shadow: rgba(0, 0, 0, 0.18);
  }
  * { margin: 0; padding: 0; box-sizing: border-box; }
  html, body {
    width: 1200px;
    height: 1000px;
    overflow: hidden;
    background: var(--page-bg);
    font-family: "Open Sans", Arial, sans-serif;
  }
  .sheet {
    position: relative;
    width: 1200px;
    height: 1000px;
  }
  .card {
    position: absolute;
    left: 290px;
    width: 620px;
    height: 354px;
    background: var(--card-white);
    box-shadow: 0 6px 18px var(--shadow);
    overflow: hidden;
  }
  .card--front { top: 110px; }
  .card--back { top: 536px; }

  /* Brand lockup */
  .brand { display: inline-block; text-align: right; }
  .brand__name {
    display: block;
    font-weight: 400;
    color: var(--ink);
    letter-spacing: 2px;
    line-height: 0.9;
    text-align: left;
  }
  .brand__tagline {
    display: block;
    font-weight: 700;
    color: var(--tag-grey);
  }

  /* Front card */
  .card--front .brand {
    position: absolute;
    left: 205px;
    top: 58px;
  }
  .card--front .brand__name { font-size: 104px; }
  .card--front .brand__tagline { font-size: 21px; margin-top: 4px; }
  .front__url {
    position: absolute;
    left: 0;
    right: 0;
    top: 222px;
    padding-left: 210px;
    font-size: 15px;
    font-weight: 700;
    letter-spacing: 2px;
    color: var(--ink-soft);
  }

  /* Back card */
  .card--back .brand {
    position: absolute;
    left: 42px;
    top: 22px;
  }
  .card--back .brand__name { font-size: 80px; }
  .card--back .brand__tagline { font-size: 17px; margin-top: 2px; }
  .back__band {
    position: absolute;
    left: 0;
    right: 0;
    top: 148px;
    bottom: 0;
    background: var(--band-cream);
  }
  .nav-dots {
    position: absolute;
    left: 38px;
    top: 170px;
    display: flex;
    gap: 28px;
  }
  .nav-dots svg { width: 44px; height: 44px; display: block; }
  .contact-list {
    position: absolute;
    left: 250px;
    top: 226px;
    list-style: none;
    font-size: 14.5px;
    color: var(--ink-soft);
    line-height: 1.3;
  }
  .contact-list__item { display: flex; }
  .contact-list__marker {
    color: var(--accent-red);
    width: 26px;
    flex: none;
    font-size: 12px;
    padding-top: 2px;
  }
</style>
</head>
<body>
<main class="sheet">

  <section class="card card--front" aria-label="Business card front">
    <div class="brand">
      <span class="brand__name">dune</span>
      <span class="brand__tagline">Shutters &amp; Blinds</span>
    </div>
    <p class="front__url">www.dunepanes.com.au</p>
  </section>

  <section class="card card--back" aria-label="Business card back">
    <div class="back__band"></div>
    <div class="brand">
      <span class="brand__name">dune</span>
      <span class="brand__tagline">Shutters &amp; Blinds</span>
    </div>

    <div class="nav-dots" aria-hidden="true">
      <svg viewBox="0 0 44 44">
        <circle cx="22" cy="22" r="20" fill="var(--dot-blue)"/>
        <circle cx="22" cy="22" r="14" fill="none" stroke="#fff" stroke-width="2"/>
        <path d="M15 22h13M23 17l5 5-5 5" fill="none" stroke="#fff" stroke-width="2.5" stroke-linecap="round" stroke-linejoin="round"/>
      </svg>
      <svg viewBox="0 0 44 44">
        <circle cx="22" cy="22" r="20" fill="var(--dot-red)"/>
        <circle cx="22" cy="22" r="14" fill="none" stroke="#fff" stroke-width="2"/>
        <path d="M15 22h13M23 17l5 5-5 5" fill="none" stroke="#fff" stroke-width="2.5" stroke-linecap="round" stroke-linejoin="round"/>
      </svg>
      <svg viewBox="0 0 44 44">
        <circle cx="22" cy="22" r="20" fill="var(--dot-yellow)"/>
        <circle cx="22" cy="22" r="14" fill="none" stroke="#fff" stroke-width="2"/>
        <path d="M15 22h13M23 17l5 5-5 5" fill="none" stroke="#fff" stroke-width="2.5" stroke-linecap="round" stroke-linejoin="round"/>
      </svg>
    </div>

    <ul class="contact-list">
      <li class="contact-list__item"><span class="contact-list__marker">&gt;&gt;</span><span>Phone : 1300 574 213</span></li>
      <li class="contact-list__item"><span class="contact-list__marker">&gt;&gt;</span><span>Email : merrow@dunepanes.com.au</span></li>
      <li class="contact-list__item"><span class="contact-list__marker">&gt;&gt;</span><span>Address : (Inside Merrow Rug Hall)<br>418 Tolvey Rd, Pelbrook VIC 3158</span></li>
      <li class="contact-list__item"><span class="contact-list__marker">&gt;&gt;</span><span>Website : www.dunepanes.com.au</span></li>
    </ul>
  </section>

</main>
</body>
</html>
```